Australian Software Consultancy needs new Business Card Design

Design Business Card based on existing design artefacts (attached). We are open to all designs. As its a 2 sided design and we thought it might be quite striking to have one side with a black background and te other side with a white background.

Target Market(s)

Financial Services mainly.

Industry/Entity Type

Business

Contact Information for Business Card

Name :
Position :
Email :

Requirements
Must have
• Funky design using our existing assets

```html
<!DOCTYPE html>
<html lang="en">
<head>
<meta charset="utf-8">
<title>Clear Orbit — Business Cards</title>
<link rel="stylesheet" href="https://fonts.googleapis.com/css2?family=Montserrat:wght@400;600;700;800&display=swap">
<style>
  :root {
    --backdrop: #ececec;
    --ink: #0a0a0a;
    --paper: #ffffff;
    --accent: #e3121c;
    --muted: #3a3a3a;
  }
  * { box-sizing: border-box; margin: 0; padding: 0; }
  html, body {
    width: 1200px;
    height: 1000px;
    overflow: hidden;
    background: var(--backdrop);
    font-family: "Montserrat", sans-serif;
  }
  .canvas {
    position: relative;
    width: 1200px;
    height: 1000px;
  }
  .card {
    position: absolute;
    width: 600px;
    height: 343px;
    display: flex;
    flex-direction: column;
    align-items: center;
    justify-content: center;
    text-align: center;
    box-shadow: 0 6px 18px rgba(0, 0, 0, 0.12);
  }
  .card--dark {
    left: 70px;
    top: 90px;
    background: var(--ink);
    color: var(--paper);
  }
  .card--light {
    left: 530px;
    top: 567px;
    background: var(--paper);
    color: var(--ink);
  }
  .brand {
    display: flex;
    align-items: center;
    gap: 14px;
    margin-bottom: 26px;
  }
  .brand__mark {
    width: 18px;
    height: 18px;
    background: var(--accent);
  }
  .brand__name {
    font-weight: 800;
    font-size: 50px;
    letter-spacing: 2px;
    line-height: 1;
  }
  .person__name {
    font-weight: 700;
    font-size: 21px;
    letter-spacing: 2px;
    line-height: 1.1;
  }
  .person__role {
    font-weight: 400;
    font-size: 11px;
    letter-spacing: 3px;
    margin-top: 4px;
    margin-bottom: 20px;
  }
  .card--dark .person__role { color: var(--accent); }
  .card--light .person__role { color: var(--muted); }
  .person__email {
    font-weight: 600;
    font-size: 27px;
    letter-spacing: 0.5px;
  }
  .card--dark .person__email { color: var(--paper); }
  .card--light .person__email { color: var(--accent); }
</style>
</head>
<body>
<main class="canvas">
  <section class="card card--dark" aria-label="Business card, black side">
    <div class="brand">
      <span class="brand__mark"></span>
      <span class="brand__name">CLEAR ORBIT</span>
    </div>
    <p class="person__name">JOHN DOE</p>
    <p class="person__role">MANAGING DIRECTOR</p>
    <p class="person__email">johndoe@clearorbit.com</p>
  </section>

  <section class="card card--light" aria-label="Business card, white side">
    <div class="brand">
      <span class="brand__mark"></span>
      <span class="brand__name">CLEAR ORBIT</span>
    </div>
    <p class="person__name">JOHN DOE</p>
    <p class="person__role">MANAGING DIRECTOR</p>
    <p class="person__email">johndoe@clearorbit.com</p>
  </section>
</main>
</body>
</html>
```